My dynamic new collection of short plays needs an eye catching web-based ad!

I am buying ad space on a theater magazine's website with these specs for a new book. The ad will run for a few months. I have the book cover - which will be the main image, but need the ad designed with quotes and the publisher's logo. Here are the specs:
230 pixels wide x 250 pixels high
72 dpi

Target Market(s)

Theater artists and theater educators

Industry/Entity Type

Theater / Education

Font styles to use
Sans Serif
Other font styles liked:
• Please use fonts that match the book cover. I'm including an ad that is currently on the website where I will be advertising. It is not the size that I'm going for, but it contains the elements that I want. I'm also including an image of the logo of the publisher, and I have other versions of this logo (other formats / larger size) that I can deliver if needed.

Requirements
Must have
• Simple compelling image with a quote from the book and a link to the publisher website. A compelling quote (or two) from the book jacket. The name and logo of the publisher.
Nice to have
• Some eye catching color to compliment the beautiful cover design
Should not have
• Too much busy-ness in the image or the presentation.

```html
<!DOCTYPE html>
<html lang="en">
<head>
<meta charset="utf-8">
<title>Lantern Hill Press – Book Ad</title>
<link rel="stylesheet" href="https://fonts.googleapis.com/css2?family=Hind:wght@400;600;700&display=swap">
<style>
  :root {
    --page-bg: #e4e4e4;
    --space-deep: #0b1430;
    --space-mid: #1b2c5c;
    --space-glow: #2d4a86;
    --text-light: #ffffff;
    --band: rgba(120, 120, 132, 0.62);
    --cover-a: #1a3f8f;
    --cover-b: #2a8fd0;
    --cover-c: #5a2d7a;
  }
  * { margin: 0; padding: 0; box-sizing: border-box; }
  html, body {
    width: 1200px; height: 1200px; overflow: hidden;
    background: var(--page-bg);
    font-family: "Hind", Arial, sans-serif;
  }
  .ad {
    position: absolute; left: 140px; top: 100px;
    width: 920px; height: 1000px; overflow: hidden;
    color: var(--text-light);
  }
  .ad-backdrop {
    position: absolute; inset: 0;
    background:
      radial-gradient(ellipse at 60% 70%, var(--space-glow) 0%, transparent 55%),
      linear-gradient(160deg, var(--space-deep) 0%, var(--space-mid) 55%, var(--space-deep) 100%);
  }
  .quote {
    position: absolute; left: 48px; top: 30px; width: 860px;
    font-size: 52px; line-height: 52px; font-weight: 400;
    white-space: nowrap;
  }
  .attribution {
    position: absolute; right: 28px; top: 274px;
    text-align: right; font-size: 48px; line-height: 60px; font-weight: 700;
    white-space: nowrap;
  }
  .book-cover {
    position: absolute; left: 32px; top: 468px;
    width: 316px; height: 560px;
    background: linear-gradient(150deg, var(--cover-a) 0%, var(--cover-b) 45%, var(--cover-c) 100%);
    box-shadow: 8px 8px 20px rgba(0,0,0,0.5);
  }
  .publisher-band {
    position: absolute; left: 360px; top: 460px;
    width: 560px; height: 304px;
    background: var(--band);
  }
  .publisher-dot {
    position: absolute; left: 232px; top: 40px;
    width: 96px; height: 96px; border-radius: 50%;
    background: var(--text-light);
  }
  .publisher-name {
    position: absolute; left: 0; top: 168px; width: 560px;
    font-size: 48px; line-height: 64px; font-weight: 400;
    letter-spacing: 4px; text-transform: uppercase; text-align: center;
  }
  .divider {
    position: absolute; left: 556px; top: 812px;
    width: 272px; height: 3px; background: var(--text-light);
  }
  .cta {
    position: absolute; left: 400px; top: 846px; width: 548px;
    text-align: center; font-size: 64px; line-height: 70px; font-weight: 600;
    white-space: nowrap;
  }
</style>
</head>
<body>
  <div class="ad">
    <div class="ad-backdrop" role="img" aria-label="Deep blue starry night sky with a soft glowing nebula"></div>
    <p class="quote">"Sam provokes us to look more<br>carefully at systems of race and<br>power and our participation in<br>them in ways that linger long after<br>the blackout."</p>
    <p class="attribution">-Mira Castell<br>Artistic Director, Brightline Stage</p>
    <div class="book-cover" role="img" aria-label="Book cover of Small Stories for a Bigger Stage by Sam Harlow, a colourful cosmic design in blues and purples"></div>
    <div class="publisher-band">
      <span class="publisher-dot"></span>
      <p class="publisher-name">Lantern Hill<br>Press</p>
    </div>
    <div class="divider"></div>
    <p class="cta">Available Now</p>
  </div>
</body>
</html>
```